PIPE RELINING COMPANY NEEDS A NEW INFORMATIVE FLYER CREATED

We are a company that sells a service to residential homeowners (using a particular state of the art international product) and we need to refresh our A4 tri- fold flyer (z fold 6 pages). The layout needs to include pictures, heading and text boxes, but be simple and clean cut at the same time.

The front of the flyer must have the attached picture of the pipe under the house, logo and website.

This flyer is going to be given to clients and to leave with them when we quote for work.

Our colour scheme is black, white, red. A highlight colour if needed (in small amounts) could be 100% cyan and also a bright orange.

I have attached the copy of the text and this can be spread out throughout the brochure.

We are a professional and industry leading company so it needs to be professional, clean cut but with a modern edge.

Target Market(s)

HOMEOWNERS

Industry/Entity Type

It Company

Font styles to use
Sans Serif

Colors
ec1f27
ffffff
000000
f37122

Requirements
Must have
• PROFESSINAL, MODERN
• USE OF BLACK, RED AND WHITE - REFER LOGO
Should not have
• BE CLUTTERED

```html
<!DOCTYPE html>
<html lang="en">
<head>
<meta charset="utf-8">
<title>Clearline Relining – Tri-fold Flyer</title>
<link href="https://fonts.googleapis.com/css2?family=Roboto+Condensed:wght@300;400;700&family=Roboto:wght@300;400&display=swap" rel="stylesheet">
<style>
  :root {
    --red: #ec1f27;
    --black: #1f1f21;
    --white: #ffffff;
    --ink: #2a2a2a;
    --paper: #f4f4f4;
    --stage: #e9e9e9;
  }
  * { box-sizing: border-box; margin: 0; padding: 0; }
  html, body { width: 1200px; height: 1200px; overflow: hidden; background: var(--stage); }
  .flyer {
    position: absolute; left: 30px; top: 194px; width: 1140px; height: 812px;
    background: var(--white); box-shadow: 0 10px 30px rgba(0,0,0,.18);
    font-family: "Roboto", sans-serif; color: var(--ink); overflow: hidden;
  }
  .inside-bg { position: absolute; left: 0; top: 0; width: 760px; height: 812px; }
  .panel { position: absolute; top: 0; width: 380px; height: 812px; }
  .panel--left { left: 0; }
  .panel--middle { left: 380px; }
  .panel--cover { left: 760px; }
  .abs { position: absolute; }
  .body-copy { font-size: 12.6px; line-height: 16px; font-weight: 300; text-align: justify; }
  .body-copy p + p { margin-top: 14px; }
  .on-dark { color: var(--white); }
  .heading {
    font-family: "Roboto Condensed", sans-serif; font-weight: 700; font-size: 13.5px; color: var(--red);
  }
  .tab {
    position: absolute; left: 0; top: 306px; width: 198px; height: 34px;
    background: var(--red); color: var(--white);
    clip-path: polygon(0 0, 100% 0, 88% 100%, 0 100%);
    font-family: "Roboto Condensed", sans-serif; font-weight: 700; font-size: 13.5px;
    padding: 9px 0 0 37px;
  }
  .steps { list-style: none; }
  .steps li { position: relative; padding-left: 14px; margin-bottom: 17px; }
  .steps li::before {
    content: ""; position: absolute; left: 0; top: 5px; width: 5px; height: 5px;
    border-radius: 50%; background: var(--red);
  }
  .callout {
    position: absolute; left: 0; top: 403px; width: 372px; height: 75px;
    background: var(--black); color: var(--white);
    font-family: "Roboto Condensed", sans-serif; font-weight: 700; font-size: 13.2px; line-height: 17px;
    padding: 11px 20px;
  }
  .footer-band {
    position: absolute; left: 0; bottom: 0; width: 380px; height: 70px; background: var(--red);
    color: var(--white); font-size: 18px; letter-spacing: 3px; font-weight: 400;
    display: flex; align-items: center; justify-content: center;
  }
  .cover-art { position: absolute; left: 0; top: 0; width: 380px; height: 545px; }
  .brand {
    position: absolute; left: 0; top: 58px; width: 380px; text-align: center;
    font-family: "Roboto Condensed", sans-serif; font-weight: 700; font-size: 46px; color: var(--white);
    letter-spacing: -0.5px;
  }
  .tagline-light {
    position: absolute; left: 0; top: 580px; width: 380px; text-align: center;
    font-family: "Roboto Condensed", sans-serif; font-weight: 400; font-size: 29px; color: var(--red);
  }
  .tagline-bold {
    position: absolute; left: 0; top: 614px; width: 380px; text-align: center;
    font-family: "Roboto Condensed", sans-serif; font-weight: 700; font-size: 37px; color: var(--black);
  }
  .service-pill {
    position: absolute; left: 30px; top: 665px; width: 310px; height: 41px;
    border: 1.5px solid var(--black); border-radius: 21px;
    font-size: 19px; font-weight: 300; color: var(--black);
    display: flex; align-items: center; justify-content: center;
  }
</style>
</head>
<body>
<main class="flyer">
  <svg class="inside-bg" viewBox="0 0 760 812" aria-hidden="true">
    <defs>
      <linearGradient id="paperShade" x1="0" y1="0" x2="1" y2="1">
        <stop offset="0" stop-color="#ececec"/>
        <stop offset="1" stop-color="#ffffff"/>
      </linearGradient>
    </defs>
    <rect width="760" height="812" fill="url(#paperShade)"/>
    <polygon points="0,0 380,0 650,108 0,288" fill="#1f1f21"/>
    <polygon points="380,0 752,0 752,140" fill="#ec1f27"/>
    <line x1="380" y1="0" x2="380" y2="812" stroke="#dddddd" stroke-width="1"/>
  </svg>

  <section class="panel panel--left">
    <h3 class="heading abs" style="left:37px; top:30px;">Which Problems Can Pipe Relining Repair?</h3>
    <div class="body-copy on-dark abs" style="left:37px; top:60px; width:297px;">
      <p>Pipe relining can repair broken, cracked or root infested pipes, pipes with missing sections and pipes that continually block.</p>
      <p>No matter if the pipes are vertical, horizontal or concealed, they all can be repaired. Sections of broken pipes can be relined, without having to replace the entire pipeline.</p>
    </div>
    <div class="tab">Patch Repair Process</div>
    <ul class="steps body-copy abs" style="left:35px; top:368px; width:308px;">
      <li>Clean the line with a high pressure water jetter, and carry out a camera inspection to determine the exact location and cause of the problems.</li>
      <li>Prepare the liner. Cut the liner to the correct length, mix the appropriate amount of rein and impregnate the rein into the liner.</li>
      <li>Invert the liner into the pipe, inflate and then cure.</li>
      <li>A seamless, flexible liner is cut to length and filled with environmentally safe epoxy rein. The liner is then inverted into the existing, host pipe and inflated using compressed air. Once the liner is fully cured with hot water, it is ready for use.</li>
      <li>The result is a completely new pipe inside the old. This pipe within a pie is 100% water tight, stronger than PVC pipe, and has an increased flow rate compared to most existing pipes. Relined pipes have a life expectancy of 50 years and our installation work has a 25 year guarantee.</li>
    </ul>
    <div class="footer-band">www.clearlinerelining.com.au</div>
  </section>

  <section class="panel panel--middle">
    <div class="body-copy abs" style="left:30px; top:190px; width:296px;">
      <p>Sewers back up in properties due to ageing lines, misaligned joints, root infestation, calcification and ground movement, costing property owners thousands of dollars in damage to their homes and landscaping.</p>
      <p>Pipe relining eliminates the need for costly excavations to expose and replace this damaged pipework.</p>
      <p>Pipe Relining is the process of installing a new pipe within the old.</p>
    </div>
    <div class="callout">Why replace all of your drainage pipes when you can permanently repair the broken sections without destroying your environment</div>
    <h3 class="heading abs" style="left:21px; top:496px;">What Does Pipe Relining Mean?</h3>
    <div class="body-copy abs" style="left:21px; top:525px; width:296px;">
      <p>Pipe relining is the method of repairing existing pipework from within the pipe itself. This is done by using the latest technology to insert a strong internal liner inside the existing pipe.</p>
      <p>During this process the resin impregnated side of the liner is pressed against the wall of the original host pipe at a specified pressure. This pressure ensure 100% resin contact and extrudes resin into all pipe joints, cracks and breaks ensuring no future tree root ingress or pipe movement is possible.</p>
      <p>Pipe relining can be undertaken in either short sectional repair, or long lengths utilising the inversion relining method.</p>
    </div>
  </section>

  <section class="panel panel--cover">
    <svg class="cover-art" viewBox="0 0 380 545">
      <defs>
        <linearGradient id="sceneTone" x1="0" y1="0" x2="0" y2="1">
          <stop offset="0" stop-color="#8fb3d6"/>
          <stop offset="0.35" stop-color="#d8ccaa"/>
          <stop offset="0.55" stop-color="#6f9a3a"/>
          <stop offset="0.75" stop-color="#8a5a3a"/>
          <stop offset="1" stop-color="#6b6358"/>
        </linearGradient>
      </defs>
      <polygon points="0,0 380,0 380,150 0,138" fill="#1f1f21"/>
      <polygon points="0,138 380,150 380,210" fill="#ec1f27"/>
      <polygon points="0,138 380,210 380,540 0,540" fill="url(#sceneTone)" role="img"
        aria-label="Photo: house on a green lawn with a tree whose roots wrap around a buried pipe cut-away"/>
    </svg>
    <div class="brand">Clearline Relining</div>
    <div class="tagline-light">Repair Pipes Without</div>
    <div class="tagline-bold">DIGGING YOUR YARD</div>
    <div class="service-pill">Pipe Relining Sydney Wide 24/7</div>
    <div class="footer-band">www.clearlinerelining.com.au</div>
  </section>
</main>
</body>
</html>
```